Restaurant Email Club Sign Up Poster

Looking for a creative design that will catch people's eye and prompt them to sign up for our email club for our Restaurant that we run in Omaha, Nebraska. Open to any creative ways to most effectively grab peoples attention quickly without being too confusing. Want it to be simple but actionable.

Have attached some documents for your assistance - in addition to some marketing materials we have put out in the past.

Would like to put design on posters to hang up throughout the restaurant and likely will make stickers to put on check presenters as well.

Catchy stock photo or use of the cheese curd photo probably good idea - callout things mentioned in the "must haves" section below. Looking for most creative and catchy, yet simple design.

Target Market(s)

30-50 year olds males and females.

Industry/Entity Type

Restaurant

Requirements
Must have
• Must include callouts for -
• Sign up for E-Club for access to future offers and events (or something along these lines)
• Free Appetizer for Signing Up
• Free Birthday Meal
Should not have
• Please do not make this poster like the postcard that I attached to the project - this is not a poster to call out that we are a new burger and beer spot, that we have 40 rotating taps, or that we have 15 specialty burgers, etc. This is simply a poster to grab someones attention and get them to sign up for our email club. Should maybe have a catchy question, something like, "Want a Free Appetizer?" or something catchy and similar, and then below say "And access to future deals and event happenings?"

```html
<!DOCTYPE html>
<html lang="en">
<head>
<meta charset="utf-8">
<title>Sign up for E-Club – Free</title>
<link rel="stylesheet" href="https://fonts.googleapis.com/css2?family=Inter+Tight:wght@800;900&display=swap">
<style>
  :root {
    --maroon: #640a35;
    --steel: #a7a8a8;
    --mint: #a8dcc0;
    --leaf: #9ccf9a;
    --sky: #b4e0f0;
  }
  html, body {
    margin: 0;
    padding: 0;
    width: 780px;
    height: 1200px;
    overflow: hidden;
    background: var(--maroon);
  }
  .poster {
    display: block;
    width: 780px;
    height: 1200px;
  }
  .poster__bg { fill: var(--maroon); }
  .poster__block { fill: var(--steel); }
  .poster__band { fill: var(--maroon); }
  .headline {
    font-family: "Inter Tight", "Helvetica Neue", Arial, sans-serif;
    font-weight: 900;
    font-size: 138px;
    letter-spacing: -6px;
    fill: var(--mint);
  }
  .headline--shadow { fill: var(--maroon); }
  .free {
    font-family: "Inter Tight", "Helvetica Neue", Arial, sans-serif;
    font-weight: 900;
    font-size: 210px;
    fill: var(--leaf);
  }
  .perks {
    font-family: "Inter Tight", "Helvetica Neue", Arial, sans-serif;
    font-weight: 800;
    font-size: 19px;
    fill: var(--sky);
  }
</style>
</head>
<body>
<svg class="poster" viewBox="0 0 500 769" preserveAspectRatio="none" xmlns="http://www.w3.org/2000/svg">
  <defs>
    <clipPath id="echo-clip">
      <rect x="0" y="250" width="500" height="185"/>
    </clipPath>
  </defs>

  <rect class="poster__bg" x="0" y="0" width="500" height="769"/>

  <g class="poster__blocks">
    <rect class="poster__block" x="152" y="0" width="348" height="435"/>
    <rect class="poster__band" x="345" y="93" width="155" height="62"/>
    <rect class="poster__band" x="486" y="155" width="14" height="97"/>
    <rect class="poster__band" x="152" y="252" width="318" height="88"/>
    <rect class="poster__band" x="470" y="252" width="30" height="88"/>
  </g>

  <text class="headline headline--shadow" x="58" y="435" textLength="322" lengthAdjust="spacingAndGlyphs" clip-path="url(#echo-clip)">Club</text>

  <g class="headline-group">
    <text class="headline" x="22" y="112" textLength="325" lengthAdjust="spacingAndGlyphs">Sign</text>
    <text class="headline" x="24" y="233" textLength="408" lengthAdjust="spacingAndGlyphs">up for</text>
    <text class="headline" x="22" y="358" textLength="450" lengthAdjust="spacingAndGlyphs">E-Club</text>
  </g>

  <text class="free" x="0" y="630" textLength="500" lengthAdjust="spacingAndGlyphs">FREE</text>

  <g class="perks">
    <text x="111" y="666" textLength="380" lengthAdjust="spacingAndGlyphs">Access to future offers and events</text>
    <text x="111" y="693" textLength="327" lengthAdjust="spacingAndGlyphs">Free Appetizer for Signing Up</text>
    <text x="111" y="719" textLength="209" lengthAdjust="spacingAndGlyphs">Free Birthday Meal</text>
  </g>
</svg>
</body>
</html>
```